TMAF inc Business Card Design

I have a rough draft of the TMAF inc logo that I would like to use on the business card. I also attached our logo for Brindlequay.com. I also included a sample of a business card from another mortgage company that I like. We would like a tagline on the back to say "let's get started" and below Brindlequay.com
Industry/Entity Type
Business
Contact Information for Business Card
Tallvane Mortgage and Funding, inc
Dale Fenwick
Mortgage Specialist
Direct (555)214-7093
Cell (555)608-1547
Fax (555)930-2861
dale@brindlequay.com
Westmarch Office of Land Registry 04728316
QFRB 417305

```html
<!DOCTYPE html>
<html lang="en">
<head>
<meta charset="utf-8">
<title>TMAF inc Business Card</title>
<link rel="stylesheet" href="https://fonts.googleapis.com/css2?family=Open+Sans:wght@400;600;700&family=Kalam:wght@400&display=swap">
<style>
  :root {
    --bg: #e9e6e1;
    --green-light: #8fbf41;
    --green-dark: #6e9f2d;
    --green-text: #7aa236;
    --navy: #1f2a5c;
    --ink: #2c3170;
    --grey-mark: #a9a9b8;
    --faint: #ededf1;
    --white: #ffffff;
  }
  * { box-sizing: border-box; margin: 0; padding: 0; }
  html, body { width: 1200px; height: 784px; overflow: hidden; }
  body {
    background: var(--bg);
    font-family: "Open Sans", Arial, sans-serif;
    position: relative;
  }
  .card {
    position: absolute;
    width: 520px;
    height: 297px;
    border-radius: 3px;
    overflow: hidden;
    box-shadow: 0 6px 18px rgba(0,0,0,.18);
  }
  /* Back side */
  .card-back {
    left: 60px; top: 80px;
    background: linear-gradient(135deg, var(--green-light), var(--green-dark));
  }
  .card-back .faint-mark {
    position: absolute; right: -20px; top: -30px;
    width: 190px; height: 190px; border-radius: 50%;
    background: rgba(255,255,255,.08);
  }
  .card-back .tagline {
    position: absolute; left: 200px; top: 110px;
    font-family: "Kalam", cursive;
    font-size: 24px; color: var(--white);
  }
  .card-back .web {
    position: absolute; left: 60px; top: 226px;
    font-size: 18px; letter-spacing: 5px; color: var(--white);
  }
  /* Front side */
  .card-front {
    left: 620px; top: 400px;
    background: var(--white);
  }
  .card-front .faint-mark {
    position: absolute; right: 28px; top: 70px;
    width: 140px; height: 140px; border-radius: 50%;
    background: var(--faint);
  }
  .person { position: absolute; right: 26px; top: 20px; text-align: left; }
  .person .name { font-size: 17px; font-weight: 700; color: var(--green-text); }
  .person .role { font-size: 10px; color: #222; margin-top: 2px; }
  .brand { position: absolute; left: 30px; top: 86px; display: flex; align-items: center; gap: 12px; }
  .brand .dot { width: 58px; height: 58px; border-radius: 50%; background: var(--grey-mark); flex: none; }
  .brand .word { font-size: 32px; font-weight: 700; color: var(--navy); line-height: 1; }
  .brand .company { font-size: 11px; font-weight: 700; color: var(--navy); margin-top: 6px; }
  .contacts { position: absolute; left: 70px; top: 172px; list-style: none; }
  .contacts li {
    display: flex; align-items: center; gap: 8px;
    font-size: 14px; line-height: 18px; color: var(--ink);
  }
  .contacts li.cont { padding-left: 22px; }
  .contacts svg { width: 14px; height: 14px; fill: var(--green-text); flex: none; }
</style>
</head>
<body>
  <section class="card card-back">
    <div class="faint-mark"></div>
    <p class="tagline">let's get started</p>
    <p class="web">Brindlequay.com</p>
  </section>

  <section class="card card-front">
    <div class="faint-mark"></div>
    <div class="person">
      <p class="name">Dale Fenwick</p>
      <p class="role">Mortgage Specialist</p>
    </div>
    <div class="brand">
      <span class="dot"></span>
      <div>
        <p class="word">TMAF inc</p>
        <p class="company">Tallvane Mortgage and Funding, inc</p>
      </div>
    </div>
    <ul class="contacts">
      <li><svg viewBox="0 0 16 16"><path d="M3 1l3 3-1.5 2a9 9 0 0 0 5.5 5.5L12 10l3 3-2 2C7 15 1 9 1 3z"/></svg>(555)214-7093</li>
      <li><svg viewBox="0 0 16 16"><path d="M4 1h8v14H4zM5.5 3v8h5V3z"/></svg>(555)608-1547</li>
      <li><svg viewBox="0 0 16 16"><path d="M4 1h8v4H4zM1 6h14v7h-3v2H4v-2H1zM5 10v4h6v-4z"/></svg>(555)930-2861</li>
      <li><svg viewBox="0 0 16 16"><path d="M1 3h14v10H1zM2 4.5v1l6 4 6-4v-1l-6 4z"/></svg>dale@brindlequay.com</li>
      <li><svg viewBox="0 0 16 16"><path d="M8 1l7 6h-2v8H9.5v-5h-3v5H3V7H1z"/></svg>Westmarch Office of Land Registry</li>
      <li class="cont">04728316 QFRB 417305</li>
    </ul>
  </section>
</body>
</html>
```